A webite for an Urgent Care for children

We need a design for a new website for an Urgent care for kids. We are based in Atlanta, GA and provide quality after-hours and urgent care services for children. We will appreciate an innovative design that employs flash technology, especially on the Home page. We also want there to be a Contact Us form. There should also be a control panel with the ability for us to make quick and minor edits on the website as needed without requiring the services of an expert.

Target Market(s)

Parents, children, general audience

Industry/Entity Type

Healthcare

Coding

Coded - Design and coding required

Number of Pages Required

5+ page

Font styles to use
Sans Serif
Decorative

Colors
acd037
acd136
cadf82
eaf2ce
f6faec

Requirements
Must have
• Mobile devices website capable
• Link to social media, Facebook, twitter, etc
Nice to have
• Ability for customers to pay online.

```html
<!DOCTYPE html>
<html lang="en">
<head>
<meta charset="utf-8">
<title>Sprout Urgent Care</title>
<link rel="stylesheet" href="https://fonts.googleapis.com/css2?family=Delius&family=Lato:wght@400;700&family=Cabin+Sketch:wght@700&display=swap">
<style>
:root{
  --green:#acd037;
  --green-mid:#cadf82;
  --green-pale:#eaf2ce;
  --green-ghost:#f6faec;
  --orange:#f26a3d;
  --orange-dark:#e2542a;
  --blue:#7fc6e8;
  --text:#3a3a3a;
  --muted:#555;
  --cream:#fdf6cf;
  --dark:#2f2f2f;
}
*{box-sizing:border-box;margin:0;padding:0}
html,body{width:796px;height:1200px;overflow:hidden}
body{position:relative;font-family:"Lato",sans-serif;color:var(--text);
  background:radial-gradient(ellipse at 85% 10%,#c8e29a 0,transparent 45%),
  radial-gradient(ellipse at 10% 60%,#cfe6a8 0,transparent 50%),
  linear-gradient(180deg,#e7f1d2 0,#d4e8b0 40%,#cfe6a6 75%,#bfe0a0 100%)}
.abs{position:absolute}
.cloud{left:40px;top:-10px;width:210px;height:112px;background:#fff;border-radius:50% 50% 50% 50%/55% 55% 45% 45%;box-shadow:0 3px 8px rgba(0,0,0,.08)}
.logo{left:78px;top:28px;width:150px;font-family:"Delius",cursive;color:#7fa81f;font-size:22px;line-height:26px;text-align:center}
.emergency{left:250px;top:5px;font-size:7.5px;font-family:"Delius",cursive;color:var(--text);display:flex;align-items:center;gap:6px}
.emergency b{font-weight:400;font-size:9.5px}
.social{top:0;width:21px;height:29px;clip-path:polygon(0 0,100% 0,100% 100%,50% 82%,0 100%)}
.nav{left:262px;top:48px;width:446px;height:30px;background:#fff;border:1px dashed var(--green);display:flex;align-items:center;padding:2px;font-family:"Delius",cursive;font-size:8px}
.nav a{color:var(--text);text-decoration:none;padding:0 8px;border-right:1px solid #999;line-height:10px}
.nav a:last-child{border:0}
.nav a.active{background:var(--green);border:0;height:24px;line-height:24px;padding:0 12px;margin-right:4px}
.hero{left:88px;top:85px;width:620px;height:264px;background:#fff;border-radius:6px;padding:4px}
.hero-inner{width:100%;height:100%;border-radius:4px;background:linear-gradient(90deg,#f3f3f3 0,#ececec 50%,#e4e4e4 100%);position:relative;overflow:hidden}
.hero-photo{position:absolute;right:0;top:0;width:330px;height:100%;background:linear-gradient(135deg,#efefef 0,#d9dde0 45%,#5b8fc4 75%,#c7ccd2 100%)}
.hero-kicker{left:20px;top:96px;font-family:"Delius",cursive;font-size:22px;color:#333}
.hero-title{left:20px;top:128px;font-family:"Cabin Sketch",sans-serif;font-size:32px;color:#222;letter-spacing:.5px}
.btn-call{left:24px;top:181px;width:130px;height:28px;background:var(--green);border:2px dashed #fff;outline:1px solid var(--green);font-family:"Delius",cursive;font-size:10px;color:#333;display:flex;align-items:center;justify-content:center}
.card{top:379px;width:198px;height:349px;background:#fff;border-radius:4px;overflow:hidden}
.card-foot{position:absolute;left:0;bottom:0;width:100%;height:44px;background:var(--cream);border-top:1px dashed #d8a36a}
.more{position:absolute;width:74px;height:25px;background:var(--orange);border:1px dashed #fff;outline:1px solid var(--orange);color:#fff;font-family:"Delius",cursive;font-size:9.5px;display:flex;align-items:center;justify-content:center}
.card .more{left:50%;margin-left:-37px;bottom:10px}
.card-h{position:absolute;width:100%;text-align:center;font-family:"Delius",cursive;color:#333}
.divider{position:absolute;left:50%;width:70px;margin-left:-35px;height:8px}
.card p,.box p{font-size:8.4px;line-height:13.5px;text-align:center;color:var(--muted)}
.services{position:absolute;left:10px;top:15px;width:178px;height:268px;background:#fff;box-shadow:0 2px 6px rgba(0,0,0,.15)}
.services ul{list-style:none;position:absolute;left:11px;top:80px;font-size:8.2px;color:var(--muted)}
.services li{height:19.6px}
.services li::before{content:"• "}
.box{left:88px;top:747px;width:620px;height:179px;background:#fff;border:3px solid #e6f1d6}
.footer{left:88px;top:948px;width:620px;height:200px;background:#fff;border-radius:6px}
.fh{position:absolute;font-family:"Delius",cursive;font-size:11px;color:#222;border-bottom:1px solid #ccc;padding-bottom:4px}
.links{position:absolute;left:17px;top:44px;list-style:none;font-family:"Delius",cursive;font-size:7.8px}
.links li{height:17.4px;padding-left:11px;position:relative}
.links li::before{content:"";position:absolute;left:0;top:3px;width:4px;height:4px;background:var(--orange)}
.field{position:absolute;left:123px;width:143px;border:1px solid #ccc;font-size:7px;color:#999;padding:6px}
.submit{position:absolute;left:125px;top:139px;width:62px;height:23px;background:var(--orange);border:1px dashed #fff;outline:1px solid var(--orange);color:#fff;font-family:"Delius",cursive;font-size:10px;display:flex;align-items:center;justify-content:center}
.ci{position:absolute;left:299px;font-size:7.5px;line-height:10.5px;color:#333}
.ci strong{font-family:"Delius",cursive;font-weight:400}
.map{position:absolute;left:442px;top:20px;width:155px;height:124px;background:linear-gradient(135deg,#eef0ee,#e2e6e2);border:2px solid #ddd}
.land{left:0;top:1096px;width:796px;height:80px;background:linear-gradient(180deg,rgba(200,230,250,0) 0,#e6f4fb 35%,#9fd04a 70%,#7fb93a 100%)}
.bar{left:0;top:1174px;width:796px;height:26px;background:var(--dark);font-family:"Delius",cursive;font-size:7.5px;color:#fff}
.bar-green{right:0;top:0;width:250px;height:26px;background:#7cb83a;clip-path:polygon(16px 0,100% 0,100% 100%,0 100%)}
.follow{right:10px;top:4px;display:flex;align-items:center;gap:4px;font-size:12px}
.follow span{width:18px;height:18px;border:1.5px solid #fff;border-radius:50%;display:inline-block}
</style>
</head>
<body>
<div class="abs cloud"></div>
<div class="abs logo">Sprout<br>Urgent Care</div>

<div class="abs emergency">If you have an emergency, please dial 911.
  <svg width="12" height="12" viewBox="0 0 24 24"><path d="M6.6 10.8a15 15 0 0 0 6.6 6.6l2.2-2.2c.3-.3.7-.4 1-.2 1.1.4 2.3.6 3.6.6.6 0 1 .4 1 1V20c0 .6-.4 1-1 1A17 17 0 0 1 3 4c0-.6.4-1 1-1h3.5c.6 0 1 .4 1 1 0 1.3.2 2.5.6 3.6.1.3 0 .7-.2 1z" fill="none" stroke="#333" stroke-width="1.6"/></svg>
  <b>(555) 201-4800</b></div>

<div class="abs social" style="left:634px;background:#3aa6dc"></div>
<div class="abs social" style="left:660px;background:#3b5b9a"></div>
<div class="abs social" style="left:686px;background:#d33a2c"></div>

<nav class="abs nav">
  <a class="active">Home</a><a>About Us</a><a>Our Services</a><a>Finance and Insurance</a><a>Office Forms</a><a>FAQ</a><a>Contact Us</a>
</nav>

<section class="abs hero">
  <div class="hero-inner">
    <div class="hero-photo" role="img" aria-label="Photo of a nurse and doctor caring for a young child in a wheelchair"></div>
    <div class="abs hero-kicker">We providing facility</div>
    <div class="abs hero-title">FOR URGENT CARE FOR KIDS</div>
    <div class="abs btn-call">Call Us : (555) 201-4800</div>
  </div>
</section>

<article class="abs card" style="left:88px">
  <div class="abs" style="left:0;top:0;width:100%;height:77px;background:linear-gradient(180deg,#f26a24,#f58a3a)"></div>
  <div class="abs" style="left:22px;top:13px;width:144px;height:116px;background:#fff;box-shadow:0 2px 5px rgba(0,0,0,.2);padding:5px">
    <div role="img" aria-label="Photo of a sleeping baby in a striped knit hat" style="width:100%;height:100%;background:linear-gradient(180deg,#8fc3ec 0,#cfe3f2 55%,#c9c9c9 100%)"></div>
  </div>
  <div class="card-h" style="top:147px;font-size:14.5px">WELCOME TO SPROUT</div>
  <svg class="divider" style="top:171px" viewBox="0 0 70 8"><line x1="0" y1="4" x2="70" y2="4" stroke="#8cbf2a"/><circle cx="35" cy="4" r="3" fill="#fff" stroke="#8cbf2a"/></svg>
  <p class="abs" style="left:12px;top:194px;width:174px">Welcome to SPROUT Urgent Care, your after-hours pediatric urgent care.<br><br>We are here when your little ones suddenly wake up sick or sustain an injury and you need immediate medical attention, but your regular doctor's office is closed...</p>
  <div class="card-foot"></div><div class="more">Read More</div>
</article>

<article class="abs card" style="left:296px">
  <div class="abs" style="left:0;top:0;width:100%;height:80px;background:var(--green)"></div>
  <div class="services">
    <div class="card-h" style="top:13px;font-size:13.5px">OUR SERVICES</div>
    <svg class="divider" style="top:38px" viewBox="0 0 70 8"><line x1="0" y1="4" x2="70" y2="4" stroke="#8cbf2a"/><circle cx="35" cy="4" r="3" fill="#fff" stroke="#8cbf2a"/></svg>
    <ul>
      <li>Same day SICK appointments</li><li>Management of simple injuries</li><li>Strains and sprains</li><li>Lacerations</li><li>Drainage of simple cysts and abscesses</li><li>Removal of foreign bodies and splints</li><li>Breathing treatments</li><li>Laceration repair</li><li>Fracture care and splinting</li><li>Lab services</li>
    </ul>
  </div>
  <div class="card-foot"></div><div class="more">Read More</div>
</article>

<article class="abs card" style="left:506px">
  <div class="abs" style="left:0;top:0;width:100%;height:75px;background:linear-gradient(180deg,#76c0e6,#a9d9f0)"></div>
  <div class="card-h" style="top:12px;font-size:14px">Dr. LUMEN</div>
  <div class="abs" style="left:41px;top:50px;width:116px;height:116px;border-radius:50%;background:#fff;border:3px dashed #cfe6a0"></div>
  <div class="abs" role="img" aria-label="Portrait photo of the doctor" style="left:49px;top:58px;width:100px;height:100px;border-radius:50%;background:linear-gradient(180deg,#d6d6d6,#6b5a50 60%,#2c2c2c)"></div>
  <p class="abs" style="left:14px;top:185px;width:170px;font-weight:700;color:#333">DANIEL O. LUMEN, M.D.; FAAP is a graduate of Northfield State University.</p>
  <p class="abs" style="left:14px;top:219px;width:170px">He attended the renowned Harlow College of Medicine, Kestrel, where he obtained his medical degree. As Sigma Chief, head of the most prestigious club in all of the region...</p>
  <div class="card-foot"></div><div class="more">Read More</div>
</article>

<section class="abs box">
  <div class="card-h" style="top:26px;font-size:13.5px">Insurance Information</div>
  <svg class="divider" style="top:46px" viewBox="0 0 70 8"><line x1="0" y1="4" x2="70" y2="4" stroke="#8cbf2a"/><circle cx="35" cy="4" r="3" fill="#fff" stroke="#8cbf2a"/></svg>
  <p class="abs" style="left:0;top:69px;width:614px;font-weight:700;color:#222">We accept most insurance plans at SPROUT Urgent Care.</p>
  <p class="abs" style="left:30px;top:87px;width:554px">We also accept patients who do not belong to any health insurance plan as cash or self-pay. If you are a self-pay patient or is self-insured, you may be eligible for a promotional self-pay discount. If your health insurance plan is not listed below, you may call or contact our office for verification.</p>
  <div class="more" style="left:271px;top:125px">Read More</div>
</section>

<footer class="abs footer">
  <div class="fh" style="left:17px;top:22px;width:70px">Quick Links</div>
  <ul class="links"><li>Home</li><li>About Us</li><li>Our Services</li><li>Finance and Insurance</li><li>Office Forms</li><li>FAQ</li><li>Contact Us</li></ul>
  <div class="fh" style="left:123px;top:22px;width:143px">Quick Contact</div>
  <div class="field" style="top:45px;height:21px">Enter your name</div>
  <div class="field" style="top:71px;height:21px">Enter your email</div>
  <div class="field" style="top:98px;height:32px">Enter your message</div>
  <div class="submit">SUBMIT</div>
  <div class="fh" style="left:299px;top:24px;width:122px;font-size:10.5px">Contact Information</div>
  <div class="ci" style="top:45px"><strong>SPROUT Urgent Care</strong><br>27 Maple Grove Court<br>Fairview, GA 30000</div>
  <div class="ci" style="top:85px">☎ (555) 201-4800<br><span style="padding-left:11px">If you have an emergency,</span><br><span style="padding-left:11px">please dial 911.</span></div>
  <div class="ci" style="top:127px">▣ (555) 201-4801</div>
  <div class="ci" style="top:146px;font-size:7px">✉ hello@sproutcareclinic.com</div>
  <div class="map" role="img" aria-label="Street map showing the clinic location"></div>
</footer>

<div class="abs land" role="img" aria-label="Illustrated landscape of clouds, green hills and trees"></div>

<div class="abs bar">
  <div class="abs" style="left:88px;top:8px">Copyright 2016 Sprout urgent care . All Right Reserved.</div>
  <div class="abs bar-green"></div>
  <div class="abs follow">Follow Us: <span></span><span></span><span></span></div>
</div>
</body>
</html>
```